14 years in business and its time for a new look and feel brochure and business cards!

We are looking to create a brochure that is professional and eye catching to bring in new commercial business. After14 years in business we have finally redone our logo and it is time to get a brochure completed as well. The logo that should be used is the one that says Inc. We want this new brochure to appeal to corporate property management companies and smaller apartment complexes. We want it to look rich and have the same high quality our work has.

Target Market(s)

property management companies and apartment complexes in the DMV.

Industry/Entity Type

Construction Company

Contact Information for Business Card

Logo
Dovid Markel
CEO
Mobile 410-555-0187
Office 410-555-0142
Address 3417 Harlow Lane Suite C Baltimore, MD 21290
Email DM@BrightCoatProsInc.example

Font styles to use
Sans Serif

Requirements
Must have
• Want the background to be black and silver gradient. Will be printing on high gloss and would like for it to be rich looking.
• brochure will be 8.5x11. open minded in terms of the fold, how it looks best with the design provided will determine that. Can be bi-fold, try-fold or z-fold.
• Content for brochure:About us
• Founded in 2003, BrightCoat Pros Inc. was the vision of Dovid Markel, with a commitment to becoming the premier renovator and developer of residential and commercial properties in the DMV. Today, BrightCoat Pros Inc. is widely respected for their gold standard in quality and efficiency and continues to grow by attracting the highest level of professionals with knowledge and experience in our field.
• BrightCoat Pros Inc.’s most valuable asset is our team members. The efforts they put forth are the key to meeting our standards and providing all of our valued clients with the highest quality of service. Leading our wonderful team members is a group of management like no other. With years of experience, the power to motivate and the keen eye to ensure top quality, our team of experts focus all of their energy to exceed our client’s expectations.
• Our Mission
• We strive to provide timely delivery, the highest level of quality and value on every project. We offer unsurpassed dedication to maintain our working relationships and consistently deliver the best service to ensure our clients success.
• Property Renovations
• BrightCoat Pros Inc. has been responsible for coordinating the construction and renovation of many projects, including all parts of a building’s interior and exterior. Well known for attention to details, quality and timely execution, BrightCoat Pros Inc. has managed and executed more than 4,000 turnovers and over 150 projects in the last 3 years alone.
• Renovations not only improve the appeal and marketability of your property, but also add value. Interior and exterior renovations help make any property more functional, energy-efficient and enable you to keep up with what your market demands. From the smallest change of a door knob to a complete kitchen overhaul, these are the things that make all the difference in your property. We are committed to deliver great value, and we do that by ensuring that our experts are involved in the renovation process, providing input and quality maintenance throughout the entire renovation.
• Services Include
• Painting
• Flooring
• Sub-Flooring
• Crown molding
• Siding & Wood Replacement
• Trim & Carpentry Work
• Punches
• Decks
• Power wash
• Concrete & Paving
• Turnovers including plumbing and electric
• Kitchen overhauls
• We offer first time clients a free apartment paint or punch on us to show you the quality you can always expect!
• Call today to schedule your first-time paint or punch at 410-555-0142.

```html
<!DOCTYPE html>
<html lang="en">
<head>
<meta charset="utf-8">
<title>BrightCoat Pros Inc. – Brochure Spread</title>
<link rel="stylesheet" href="https://fonts.googleapis.com/css2?family=Cinzel:wght@400;600&family=Oswald:wght@600&family=Open+Sans:wght@600;700&display=swap">
<style>
  :root {
    --canvas: #ececec;
    --paper: #ffffff;
    --silver-light: #8d8d90;
    --silver-mid: #76777b;
    --silver-dark: #5d5e62;
    --ink: #111111;
    --ink-grey: #6d6e72;
    --white: #ffffff;
  }
  * { margin: 0; padding: 0; box-sizing: border-box; }
  html, body { width: 1200px; height: 1200px; overflow: hidden; background: var(--canvas); }
  .spread {
    position: absolute; left: 40px; top: 200px;
    width: 1120px; height: 800px; display: flex;
  }
  .page { position: relative; width: 560px; height: 800px; overflow: hidden; }
  .page svg.art { position: absolute; inset: 0; }

  .brand {
    position: absolute; display: flex; align-items: center; gap: 8px;
    font-family: "Open Sans", sans-serif; font-weight: 700; white-space: nowrap;
  }
  .brand-dot { width: 14px; height: 14px; border-radius: 50%; }

  /* back cover */
  .back .brand { left: 0; right: 0; top: 205px; justify-content: center; color: var(--white); font-size: 19px; }
  .back .brand-dot { background: var(--white); }
  .call-title {
    position: absolute; left: 0; right: 0; top: 312px; text-align: center;
    font-family: "Cinzel", serif; font-weight: 600; font-size: 20px; color: var(--white);
  }
  .call-text {
    position: absolute; left: 0; right: 0; top: 346px; text-align: center;
    font-family: "Cinzel", serif; font-size: 14px; line-height: 18px; color: var(--white);
  }
  .call-text strong { font-weight: 600; }

  /* front cover */
  .front { background: var(--paper); }
  .front .brand { right: 55px; top: 92px; color: var(--ink-grey); font-size: 21px; }
  .front .brand-dot { background: var(--ink-grey); }
  .headline {
    position: absolute; right: 45px; top: 550px; white-space: nowrap;
    font-family: "Oswald", sans-serif; font-weight: 600; font-size: 48px; line-height: 56px;
    color: var(--ink); letter-spacing: -0.5px;
    transform: scaleX(0.85); transform-origin: right center;
  }
  .subhead {
    position: absolute; right: 45px; top: 604px; white-space: nowrap;
    font-family: "Cinzel", serif; font-weight: 600; font-size: 60px; line-height: 66px;
    color: var(--ink-grey);
  }
  .offer {
    position: absolute; left: 90px; width: 400px; top: 683px; text-align: center;
    font-family: "Open Sans", sans-serif; font-weight: 600; font-size: 15.5px; line-height: 22px;
    color: var(--ink); white-space: nowrap;
  }
  .quote-mark {
    position: absolute; font-family: "Cinzel", serif; font-weight: 600; font-size: 52px;
    line-height: 1; color: var(--ink-grey);
  }
  .quote-open { left: 88px; top: 676px; }
  .quote-close { left: 398px; top: 722px; }
</style>
</head>
<body>
<main class="spread">

  <section class="page back">
    <svg class="art" width="560" height="800" viewBox="0 0 560 800">
      <defs>
        <linearGradient id="silverBack" x1="0" y1="0" x2="1" y2="0">
          <stop offset="0" stop-color="var(--silver-dark)"/>
          <stop offset="0.45" stop-color="var(--silver-light)"/>
          <stop offset="1" stop-color="var(--silver-dark)"/>
        </linearGradient>
        <linearGradient id="painterTones" x1="0" y1="0" x2="1" y2="1">
          <stop offset="0" stop-color="#f4f4f4"/>
          <stop offset="0.6" stop-color="#d9d9d9"/>
          <stop offset="1" stop-color="#8f8f8f"/>
        </linearGradient>
      </defs>
      <rect class="back-bg" width="560" height="800" fill="url(#silverBack)"/>
      <path d="M0,547 C180,480 380,436 560,430 L560,800 L0,800 Z" fill="url(#painterTones)"
            role="img" aria-label="Photo: painter rolling white paint onto an interior wall"/>
    </svg>
    <div class="brand"><span class="brand-dot"></span>BrightCoat Pros Inc.</div>
    <h2 class="call-title">Call Today</h2>
    <p class="call-text">TO SCHEDULE YOUR FIRST-TIME PAINT OR<br>PUNCH AT <strong>410-555-0142</strong></p>
  </section>

  <section class="page front">
    <svg class="art" width="560" height="800" viewBox="0 0 560 800">
      <defs>
        <linearGradient id="spineShade" x1="0" y1="0" x2="1" y2="0">
          <stop offset="0" stop-color="#dedede"/>
          <stop offset="0.15" stop-color="#ffffff"/>
        </linearGradient>
        <linearGradient id="swooshGrey" x1="0" y1="0" x2="1" y2="0">
          <stop offset="0" stop-color="#9a9a9d"/>
          <stop offset="1" stop-color="var(--silver-mid)"/>
        </linearGradient>
        <linearGradient id="facadeTones" x1="0" y1="0" x2="1" y2="1">
          <stop offset="0" stop-color="#e8e4dc"/>
          <stop offset="0.5" stop-color="#b9c6d2"/>
          <stop offset="1" stop-color="#5f6d78"/>
        </linearGradient>
      </defs>
      <rect width="560" height="800" fill="url(#spineShade)"/>
      <path class="swoosh" d="M0,418 C160,400 400,418 560,478 L560,528 C420,470 240,432 0,428 Z" fill="url(#swooshGrey)"/>
      <circle class="crescent" cx="259" cy="326" r="186" fill="var(--silver-mid)"/>
      <circle cx="241" cy="311" r="180" fill="url(#facadeTones)"
              role="img" aria-label="Photo: painter in a safety harness rolling paint on a high-rise exterior"/>
    </svg>
    <div class="brand"><span class="brand-dot"></span>BrightCoat Pros Inc.</div>
    <h1 class="headline">GOLD STANDARD IN QUALITY</h1>
    <p class="subhead">&amp; EFFICIENCY</p>
    <span class="quote-mark quote-open">“</span>
    <p class="offer">We offer first time clients a free apartment<br>paint or punch on us to show you the quality<br>you can always expect!</p>
    <span class="quote-mark quote-close">”</span>
  </section>

</main>
</body>
</html>
```